Medical Breast Thermography Brochure Needed

Looking for a brochure that matches the theme and overall look/feel of our website brightoakcare.com.

http://brightoakcare.com/ourservices/breast-thermography/

I have previously used PixelVenue for logo, business card, and brochure and have been very happy, as soon as designs start being submitted I will switch to guaranteed payment.

I'm looking for a professional, clean, simple, minimalist, bold design.
Colors would ideally be greens and blues, or pink, cool tones, muted colors, or graytones.

See attached word document for content for brochure.

I would like to have the TH1-TH5 images in the Vantora thermo brochure 11.pdf document in the brochure.

Also would like one fold to compare mammogram with breast thermography like in BOCM_thermography_vs_mammography.jpg

I have attached a copy of our prior overall practice brochure to see what type of design I would like.

Feel free to use any stock photos.

```html
<!DOCTYPE html>
<html lang="en">
<head>
<meta charset="utf-8">
<title>Breast Thermography Brochure – Bright Oak Care Medicine</title>
<link href="https://fonts.googleapis.com/css2?family=Cinzel:wght@400;600&family=Oswald:wght@500&family=Roboto:wght@400;500;700&display=swap" rel="stylesheet">
<style>
:root{
  --backdrop:#e7e4df;
  --paper:#ffffff;
  --blue:#1f6f98;
  --blue-dark:#1b5f86;
  --green:#7cb342;
  --green-dark:#5d9a2c;
  --pink:#e2197a;
  --ink:#333333;
  --sky-top:#cfe4f3;
  --sky-bottom:#eef5f8;
}
*{margin:0;padding:0;box-sizing:border-box}
html,body{width:1200px;height:1200px;overflow:hidden;background:var(--backdrop)}
body{position:relative;font-family:'Roboto',sans-serif;color:var(--ink)}
.page{position:absolute;width:399px;height:559px;background:var(--paper);overflow:hidden;box-shadow:0 4px 14px rgba(0,0,0,.25)}
.cover{left:125px;top:33px;background:linear-gradient(180deg,var(--sky-top),var(--sky-bottom) 55%)}
.inside-left{left:681px;top:33px}
.inside-back{left:416px;top:617px}
.abs{position:absolute}

/* cover */
.brand{left:0;right:0;top:38px;text-align:center}
.brand-name{font-family:'Roboto',sans-serif;font-weight:700;font-size:34px;color:var(--blue);letter-spacing:.5px}
.brand-sub{font-family:'Roboto',sans-serif;font-weight:700;font-size:10px;color:var(--blue);letter-spacing:4px;margin-top:2px}
.cover-title{left:0;right:0;top:148px;text-align:center;font-family:'Cinzel',serif;font-weight:600;font-size:26px;color:var(--blue)}
.cover-title span{color:var(--green)}
.cover-tag{left:0;right:0;top:188px;text-align:center;font-size:13px;font-weight:500;color:#222;letter-spacing:.2px}
.cover-tag i{font-style:normal;color:#888;margin:0 6px}
.cover-photo{left:0;top:290px;width:399px;height:269px;background:linear-gradient(160deg,#e9cbb0 0%,#c89b7b 35%,#8fae62 60%,#d8b79a 100%)}

/* inside text */
.head{font-size:9.5px;font-weight:500;color:var(--blue);line-height:1.25}
.head span{color:var(--green)}
.body{font-size:6px;line-height:1.35}
.strong{font-weight:700}
ul.ticks{list-style:none}
ul.ticks li{position:relative;padding-left:13px;font-size:6px;line-height:1.3;margin-bottom:6px}
ul.ticks li::before{content:"";position:absolute;left:2px;top:1px;width:3px;height:6px;border:solid var(--green);border-width:0 1.5px 1.5px 0;transform:rotate(40deg)}
ul.big li{font-size:9px;margin-bottom:4px}
ul.big li::before{top:2px}
ul.tight li{margin-bottom:3px;font-size:5.6px}
.rule{display:inline-block;border-bottom:1px solid #9bbfd4;padding-bottom:2px}

.photo-circle{border-radius:50%;border:4px solid var(--blue);outline:3px solid var(--green);outline-offset:1px}
.banner{left:24px;top:229px;width:350px;height:34px;background:var(--blue-dark);border-radius:6px;box-shadow:0 0 0 2px #9ccbe3;color:#fff;text-align:center;font-family:'Cinzel',serif;font-size:9px;line-height:1.3;padding-top:5px}
.stat-icons{left:24px;top:412px;width:156px;height:34px;background:linear-gradient(90deg,#333 0 50%,var(--pink) 50% 62%,#333 62%);opacity:.85;border-radius:3px}
.stat-big{left:24px;top:452px;font-family:'Oswald',sans-serif;font-weight:500;font-size:30px;color:var(--pink);line-height:1}
.stat-small{left:24px;top:490px;font-family:'Oswald',sans-serif;font-weight:500;font-size:12.5px;color:#222}
.right-col{left:200px;top:398px;width:180px}
.right-col li{text-align:justify}
.wave{left:0;bottom:0;width:399px;height:32px}
</style>
</head>
<body>

<section class="page cover">
  <div class="abs brand">
    <div class="brand-name">Bright Oak</div>
    <div class="brand-sub">CARE MEDICINE</div>
  </div>
  <h1 class="abs cover-title">Breast <span>Thermography</span></h1>
  <p class="abs cover-tag">SAFE SCREENING<i>|</i>EARLY DETECTION</p>
  <div class="abs cover-photo" role="img" aria-label="Photo of a smiling family of four outdoors, children on parents' backs"></div>
</section>

<section class="page inside-left">
  <h2 class="abs head" style="left:24px;top:22px">Now You Don't Have To Wait Till Your Next MammoGram<br><span>To Get a Window Into Your Breast Health!</span></h2>
  <p class="abs body" style="left:24px;top:48px;width:230px">Whether you are a busy mom of three, a retired grandmother, or a working woman, your health is your most valuable asset, and you try your best to be on top of taking care of your health.</p>
  <p class="abs body strong" style="left:24px;top:86px">So, what about your breast health?<br>Have you had your breast-health checked recently?</p>
  <h3 class="abs head" style="left:24px;top:113px"><span class="rule">Perhaps <span>You:</span></span></h3>
  <ul class="abs ticks" style="left:24px;top:135px;width:210px">
    <li>Have a family history of breast cancer but are too young for a mammogram</li>
    <li>Are worried about toxic radiation exposure from mammograms</li>
    <li>You have had surgery, implants, or biopsies that might make mammograms difficult to interpret</li>
    <li>Have had an inconclusive mammogram</li>
    <li>Are just plain worried about your breast health</li>
  </ul>
  <div class="abs photo-circle" style="left:242px;top:69px;width:134px;height:134px;background:radial-gradient(circle at 45% 55%,#f07a7a 0,#f3c9c0 25%,#ebe6e4 60%)" role="img" aria-label="Photo of a woman holding her hand over her breast"></div>
  <div class="abs banner">No Matter Which Situation You Are In,<br>Bright Oak Care Medicine Has The Perfect Solution For You!</div>
  <h3 class="abs head" style="left:24px;top:278px"><span class="rule">Why <span style="color:var(--blue)">Breast Health?</span></span></h3>
  <ul class="abs ticks" style="left:24px;top:298px;width:355px">
    <li>As you already know, breast health is incredibly important, and breast problems can develop silently for decades before anything can be picked up on a mammogram!</li>
    <li>Every 2 minutes a woman is diagnosed with Breast Cancer</li>
    <li>Every 13 minutes a woman in the US loses her life to breast cancer</li>
    <li>More than 250,000 women under 40 in the US live with a breast cancer diagnosis.</li>
    <li>About one in eight women in the U.S. will develop invasive breast cancer during her lifetime.</li>
  </ul>
  <div class="abs stat-icons" role="img" aria-label="Pictogram of eight women figures, one highlighted in pink"></div>
  <div class="abs stat-big">1 IN 8 WOMEN</div>
  <div class="abs stat-small">WILL DEVELOP BREAST CANCER</div>
  <ul class="abs ticks right-col">
    <li>Breast cancer is the most common cancer in American women, behind skin cancer, and second-leading cause of cancer death in women, exceeded only by lung cancer.</li>
    <li>An estimated 232,670 new cases of invasive breast cancer will be diagnosed in U.S. women this year.</li>
    <li>Two of three breast cancers are found in women 55 or older and approximately 1/3 of all breast cancers occur in women under 45.</li>
    <li>Here at Bright Oak Care Medicine, we don't just deal with problems after they have formed. We pride ourselves on comprehensive, preventive health-care to keep you happy and healthy, and this is why we have developed a comprehensive Breast Health Screening Program using state-of-the-art <b><i>Breast Thermography.</i></b></li>
  </ul>
  <svg class="abs wave" viewBox="0 0 399 32" preserveAspectRatio="none"><path d="M0 22 C120 4 260 4 399 12 V32 H0Z" fill="var(--green)"/><path d="M0 20 C120 2 260 2 399 10" fill="none" stroke="#b7d98f" stroke-width="1.5"/></svg>
</section>

<section class="page inside-back">
  <h2 class="abs head" style="left:24px;top:22px"><span class="rule">What is Breast <span>Thermography?</span></span></h2>
  <div class="abs body" style="left:24px;top:42px;width:352px;text-align:justify">
    <p style="margin-bottom:7px">Breast Thermography is an exciting addition to breast imaging technology that was approved by the FDA in 1982. It is an additional tool that doctors use to help determine breast cancer risk and can also indicate the risk of other breast conditions. When Breast Thermography is used in combination with other tests, it gives your doctor an improved overall picture of breast health.</p>
    <p style="margin-bottom:7px">Breast Thermography uses infra-red imaging technology to scan the breast and produces an incredibly detailed heat map, which can help detect the new blood vessels that grow from tumors, as well as hormonal imbalances, and other breast-health problems.</p>
    <p>Breast thermography provides an additional piece of the puzzle and is not to be used alone. However, when used together with other imaging and lab tests, it will provide your doctor with much more information, giving a more comprehensive picture of your overall breast health.</p>
  </div>
  <h3 class="abs head" style="left:24px;top:149px"><span class="rule">Benefits of Breast <span>Thermography</span></span></h3>
  <ul class="abs ticks big" style="left:24px;top:168px;width:205px">
    <li>Safe</li>
    <li>Painless</li>
    <li>No harmful radiation</li>
    <li>Can be used at any age</li>
    <li>No limit on number of tests you can have per year</li>
    <li>Fast</li>
  </ul>
  <div class="abs photo-circle" style="left:239px;top:161px;width:130px;height:130px;border-color:var(--blue-dark);background:radial-gradient(circle at 40% 45%,#2b8cff 0,#37d16b 25%,#e7e52a 45%,#e3402a 70%,#2a1a70 100%)" role="img" aria-label="Thermal heat-map image of a chest"></div>
  <h3 class="abs head" style="left:24px;top:290px"><span class="rule">Who should have <span>Breast Thermography?</span></span></h3>
  <ul class="abs ticks tight" style="left:24px;top:312px;width:360px">
    <li>Women with Fibrocystic Breasts or Dense Breasts.</li>
    <li>Dense breast tissue contains more glands and ligaments and less fat. Mammograms have trouble seeing through dense tissue; however thermograms can easily evaluate dense breast tissue.</li>
    <li>Women with inconclusive mammograms.</li>
    <li>Thermography can reduce the need for biopsies by up to 20%.</li>
    <li>Women with surgical implants.</li>
    <li>The risk of an implant rupturing during a mammogram is a small, but valid concern. With thermography there is no compression and no risk!</li>
    <li>Younger women who want to limit radiation exposure to the breast.</li>
    <li>A routine mammogram consists of two views of each breast and contains up to 0.2 rad per x-ray. Radiation accumulates in breast tissue, and each 1.0 rad of exposure increases the risk of breast cancer by 1 percent. Because thermography images thermal heat emanating from the body, there is no radiation risk whatsoever.</li>
    <li>Women with a family history of breast cancer.</li>
    <li>Annual breast screening is not usually recommended until age 40; however, if you fall into the high risk category, thermograms should be started in the mid 20's in order to obtain a baseline for all future comparisons.</li>
    <li>Women struggling with hormone imbalance.</li>
    <li>Women who want a baseline for overall breast health.</li>
    <li>Women who have had surgical procedures or biopsies to the breast.</li>
    <li>Women who have had a mastectomy.</li>
    <li>You have had an abnormal mammogram and have been told you need to wait 6 months before your next mammogram</li>
    <li>Any man or woman concerned about breast health.</li>
  </ul>
  <svg class="abs wave" viewBox="0 0 399 32" preserveAspectRatio="none"><path d="M0 22 C120 4 260 4 399 12 V32 H0Z" fill="var(--green)"/><path d="M0 20 C120 2 260 2 399 10" fill="none" stroke="#b7d98f" stroke-width="1.5"/></svg>
</section>

</body>
</html>
```